Commercial Loan Originator Business Card (CHANGE COLORS SCHEME)

CHANGE COLOR SCHEME - SAME DESIGN

Name Miranda Lestock
Title Commercial Loan Originator
Office (800) 641-2905 x68
Direct (240) 731-2264
Email gardenpath4life@mailbox.example

Name Dale Fenwick
Office (800) 641-2905 x70
Direct (410) 392-6058
Email d.fenwickhomes@mailbox.example

Name Gerald Winslow
Office (800) 641-2905 x71
Direct (215) 946-3021
Email g.winslow63@mailbox.example

Name Joan Mallory
Office (800) 641-2905 x
Direct (202) 518-4467
Email jmallory74@mailbox.example

Name Norah Velasco
Office (800) 641-2905 x72
Direct (240) 867-1152
Email capitalhomelending@mailbox.example

```html
<!DOCTYPE html>
<html lang="en">
<head>
<meta charset="utf-8">
<title>Joan Mallory – Commercial Loan Originator</title>
<link rel="stylesheet" href="https://fonts.googleapis.com/css2?family=Crimson+Text:wght@600&family=Poppins:wght@400&display=swap">
<style>
  :root {
    --page-bg: #8a8a8a;
    --card-bg: #ffffff;
    --brand-primary: #0e6e6a;
    --brand-accent: #e0a32e;
    --ink: #1d1d1f;
    --photo-light: #e9e4ef;
    --photo-mid: #8d5fa6;
    --photo-dark: #2b2f52;
  }
  * { margin: 0; padding: 0; box-sizing: border-box; }
  html, body {
    width: 1200px; height: 952px; overflow: hidden;
    background: var(--page-bg);
  }
  .business-card {
    position: absolute; left: 60px; top: 143px;
    width: 1080px; height: 666px;
    background: var(--card-bg);
    border-radius: 42px;
    overflow: hidden;
  }
  .card-art { position: absolute; inset: 0; width: 100%; height: 100%; }
  .name-accent {
    position: absolute; left: 0; top: 92px;
    width: 26px; height: 65px;
    background: var(--brand-primary);
  }
  .holder-name {
    position: absolute; left: 46px; top: 84px;
    font-family: "Crimson Text", serif; font-weight: 600;
    font-size: 52px; line-height: 1; letter-spacing: 0.5px;
    color: var(--brand-primary); text-transform: uppercase;
  }
  .holder-title {
    position: absolute; left: 46px; top: 130px;
    font-family: "Poppins", sans-serif; font-size: 31px;
    color: var(--ink); line-height: 1.2;
  }
  .contact-list {
    position: absolute; left: 50px; top: 313px;
    list-style: none;
    font-family: "Poppins", sans-serif; font-size: 32px;
    color: var(--ink);
  }
  .contact-list li {
    display: flex; align-items: center; height: 39px;
  }
  .contact-icon { width: 32px; height: 32px; margin-right: 15px; flex: none; }
  .contact-note { color: var(--brand-primary); margin-left: 10px; }
</style>
</head>
<body>
  <div class="business-card">
    <svg class="card-art" viewBox="0 0 1080 666" preserveAspectRatio="none">
      <defs>
        <radialGradient id="portrait-tone" cx="0.5" cy="0.55" r="0.5">
          <stop offset="0" stop-color="var(--photo-dark)"/>
          <stop offset="0.5" stop-color="var(--photo-mid)"/>
          <stop offset="0.85" stop-color="var(--photo-light)" stop-opacity="0.6"/>
          <stop offset="1" stop-color="var(--photo-light)" stop-opacity="0"/>
        </radialGradient>
      </defs>
      <path class="wave-accent" d="M0,497 C90,474 190,462 270,469 C390,480 540,525 660,560 L900,630 L0,640 Z" fill="var(--brand-accent)"/>
      <ellipse role="img" aria-label="Portrait photo of the loan originator smiling and waving" cx="800" cy="400" rx="340" ry="400" fill="url(#portrait-tone)"/>
      <path class="wave-primary" d="M0,558 C110,510 220,497 300,500 C450,508 600,560 760,602 C840,622 920,622 1080,588 L1080,666 L0,666 Z" fill="var(--brand-primary)"/>
      <path class="wave-divider" d="M0,558 C110,510 220,497 300,500 C450,508 600,560 760,602 C840,622 920,622 1080,588" fill="none" stroke="#fff" stroke-width="6"/>
    </svg>

    <div class="name-accent"></div>
    <h1 class="holder-name">Joan Mallory</h1>
    <p class="holder-title">Commercial Loan Originator</p>

    <ul class="contact-list">
      <li>
        <svg class="contact-icon" viewBox="0 0 32 32"><path d="M9 5 L13 11 L10.5 14 C12 17.5 14.5 20 18 21.5 L21 19 L27 23 L25 27 C16 28 5 17 5 8 Z" fill="none" stroke="var(--brand-primary)" stroke-width="2.6" stroke-linejoin="round"/><path d="M18 9 A6 6 0 0 1 23 14 M18 4 A11 11 0 0 1 28 14" fill="none" stroke="var(--brand-primary)" stroke-width="2.4" stroke-linecap="round"/></svg>
        <span>(800) 641-2905 x</span>
      </li>
      <li>
        <svg class="contact-icon" viewBox="0 0 32 32"><path d="M9 5 L13 11 L10.5 14 C12 17.5 14.5 20 18 21.5 L21 19 L27 23 L25 27 C16 28 5 17 5 8 Z" fill="none" stroke="var(--brand-primary)" stroke-width="2.6" stroke-linejoin="round"/><path d="M18 9 A6 6 0 0 1 23 14 M18 4 A11 11 0 0 1 28 14" fill="none" stroke="var(--brand-primary)" stroke-width="2.4" stroke-linecap="round"/></svg>
        <span>(202) 518-4467</span><span class="contact-note">(Direct )</span>
      </li>
      <li>
        <svg class="contact-icon" viewBox="0 0 32 32"><rect x="2" y="7" width="28" height="19" fill="var(--brand-primary)"/><path d="M2 7 L16 18 L30 7 M2 26 L12 15 M30 26 L20 15" fill="none" stroke="#fff" stroke-width="2"/></svg>
        <span>jmallory74@mailbox.example</span>
      </li>
    </ul>
  </div>
</body>
</html>
```